pelbrook Web Design Project

It is a virtual assistance/concierge company that helps the busy professional by remotely providing administrative, technical and/or creative business support services, specializing in the medical device industry. Company name is pelbrook.
(website will be pelbrook-demo.net)

Allowing things to be done without taking time away from more urgent issues or family/personal time. Partnering with a VA reduces stress, protects cash flow, eliminates administrative hassles, and enables business people to find the success they originally set out to achieve. Saves small businesses and/or individuals on overhead, salary, et. Work is done remotely to offer administrative, clerical, typing and specialist service assistance on a regular, ad-hoc or emergency cover basis.

Though we are capable of addressing the needs of medical professionals and industry representatives due to our experience and knowledge (sales, HCC guidelines, etc.) we do not want to be limited to that market only.

Target Market(s)

Target market would be M/F, 30-50, National, busy, Alpha, entrepreneurs and industry professionals who want/need to do more without sacrifice of life

Industry/Entity Type

Industry

Requirements
Nice to have
• We do have a logo designed via the ArtHively website that can/should be included. Logo is uploaded.

```html
<!DOCTYPE html>
<html lang="en">
<head>
<meta charset="utf-8">
<title>pelbrook – virtual assistance</title>
<link rel="stylesheet" href="https://fonts.googleapis.com/css2?family=Exo+2:ital,wght@0,400;0,500;1,400&family=PT+Sans:wght@400;700&display=swap">
<style>
:root{
  --sky:#a2cad8;
  --navy:#1e3a5f;
  --ink:#2a3240;
  --grey-text:#707070;
  --soft:#ececec;
  --red:#d3232a;
  --link:#1f3566;
  --footer:#111821;
  --white:#ffffff;
  --icon:#243e63;
}
*{box-sizing:border-box;margin:0;padding:0}
html,body{width:1040px;height:1200px;overflow:hidden}
body{background:linear-gradient(160deg,#b3d6e2 0%,var(--sky) 50%,#9fc7d6 100%);font-family:"PT Sans",sans-serif;position:relative}
.topbar{position:absolute;left:146px;top:20px;display:flex;gap:14px;font-size:9px;color:var(--ink);align-items:center}
.topbar span{display:flex;align-items:center;gap:5px}
.site{position:absolute;left:123px;top:54px;width:800px}
.header{height:67px;background:linear-gradient(#fff,#f7f7f7);border-radius:3px 3px 0 0;position:relative;box-shadow:0 1px 3px rgba(0,0,0,.15)}
.brand{position:absolute;left:16px;top:14px;display:flex;align-items:center;gap:6px;font-family:"Exo 2",sans-serif;font-size:32px;font-weight:500;color:var(--navy);line-height:1}
.brand .dot{width:14px;height:14px;border-radius:50%;background:var(--red)}
.nav{position:absolute;right:14px;top:22px;display:flex;font-family:"Exo 2",sans-serif;font-size:14px;color:var(--ink)}
.nav a{color:inherit;text-decoration:none;padding:4px 0;text-align:center}
.nav .home{width:67px;background:#efefef;border:1px solid #e0e0e0;border-radius:2px;color:var(--red);margin-right:13px}
.nav a:nth-child(2){width:67px}.nav a:nth-child(3){width:78px}.nav a:nth-child(4){width:60px}.nav a:nth-child(5){width:84px}.nav a:nth-child(6){width:60px}
.hero{position:relative;height:271px;background:linear-gradient(100deg,#9ad0ea 0%,#3e7fa6 35%,#1f4b6d 65%,#173a58 100%)}
.caption{position:absolute;left:0;right:0;bottom:0;height:46px;background:rgba(180,200,215,.55);display:flex;align-items:center}
.caption h1{font-family:"Exo 2",sans-serif;font-style:italic;font-weight:400;font-size:27px;letter-spacing:2px;color:#15284a;margin-left:27px;width:364px}
.caption p{font-size:9.5px;font-style:italic;color:#fff;line-height:14px;width:390px}
.redbar{height:6px;background:var(--red)}
.features{height:80px;background:var(--soft);position:relative}
.feature{position:absolute;top:16px;display:flex;gap:14px}
.feature .badge{width:46px;height:46px;border-radius:50%;background:var(--icon);display:flex;align-items:center;justify-content:center}
.feature h3{font-family:"Exo 2",sans-serif;font-weight:400;font-size:15px;color:var(--navy);margin-top:0}
.feature p{font-size:9px;color:var(--grey-text);line-height:12px;margin-top:3px}
.content{background:var(--white);height:585px;position:relative;margin:0 1px}
.headline{position:absolute;left:20px;font-family:"Exo 2",sans-serif;font-weight:400;font-size:15px;color:#333;border-bottom:1px solid #ddd;padding-bottom:6px}
.headline::after{content:"";position:absolute;left:0;bottom:-2px;width:162px;height:2px;background:var(--red)}
.intro{position:absolute;left:20px;top:60px;width:760px;font-size:9.6px;line-height:19.4px;color:var(--grey-text)}
.intro b{font-weight:400;color:var(--link)}
.intro p+p{margin-top:19px}
.more{color:var(--red);margin-left:4px}
.card{position:absolute;top:247px;width:232px}
.card .photo{height:137px}
.card h4{display:flex;align-items:center;gap:9px;font-family:"Exo 2",sans-serif;font-weight:400;font-size:14px;color:var(--navy);margin-top:6px}
.card p{font-size:8.5px;color:var(--grey-text);margin:4px 0 0 26px}
.card p span{color:var(--red);font-size:11px}
.quote{position:absolute;left:20px;top:471px;width:760px;height:84px;background:var(--soft)}
.quote .mark{position:absolute;left:14px;top:8px}
.quote p{position:absolute;left:80px;top:14px;width:660px;font-family:"Exo 2",sans-serif;font-style:italic;font-size:15px;line-height:29px;letter-spacing:.7px;color:#6b6b6b}
.quote cite{color:var(--red);font-style:italic}
.footer{position:absolute;left:124px;top:1085px;width:798px;height:52px;background:var(--footer);color:#fff;font-size:9px;font-weight:700;display:flex;align-items:center;justify-content:space-between;padding:0 19px 0 21px}
.footer nav{display:flex;gap:17px}
.footer nav a{color:#fff;text-decoration:none}
.footer nav .active{color:var(--red);margin-right:7px}
</style>
</head>
<body>
<div class="topbar">
  <span><svg width="10" height="12" viewBox="0 0 10 12"><path d="M2 1l2 2-1 2c1 2 2 3 4 4l1-1 2 2-2 2C4 11 0 7 0 3z" fill="#1e3a5f"/></svg>12345 1234567</span>
  <span><svg width="11" height="8" viewBox="0 0 11 8"><rect width="11" height="8" fill="#1e3a5f"/><path d="M0 0l5.5 4L11 0" stroke="#a2cad8" fill="none"/></svg>contact@pelbrook-demo.net</span>
</div>

<div class="site">
  <header class="header">
    <div class="brand"><span class="dot"></span>pelbrook</div>
    <nav class="nav"><a class="home">home</a><a>about</a><a>join</a><a>blog</a><a>FAQ</a><a>contact</a></nav>
  </header>
  <section class="hero" role="img" aria-label="Photo of a professional touching a glowing world map on a digital interface">
    <div class="caption">
      <h1>Your time, your business</h1>
      <p>pelbrook is a virtual assistance company helping busy professionals by remotely providing admin, technical &amp; creative business support services</p>
    </div>
  </section>
  <div class="redbar"></div>
  <section class="features">
    <div class="feature" style="left:22px"><div class="badge"><svg width="24" height="22" viewBox="0 0 24 22"><rect x="1" y="1" width="22" height="14" fill="none" stroke="#fff" stroke-width="2.5"/><rect x="9" y="15" width="6" height="3" fill="#fff"/><rect x="6" y="18" width="12" height="2" fill="#fff"/></svg></div><div><h3>Icon Title One</h3><p>Lorem ipsum dolor sit am<br>consectetur adipiscing</p></div></div>
    <div class="feature" style="left:223px"><div class="badge"><svg width="22" height="20" viewBox="0 0 22 20"><path d="M2 1v17h19" stroke="#fff" stroke-width="2.5" fill="none"/><path d="M5 14l5-5 3 3 6-6" stroke="#fff" stroke-width="2.5" fill="none"/><path d="M15 5h5v5" stroke="#fff" stroke-width="2" fill="none"/></svg></div><div><h3>Icon Title Two</h3><p>Lorem ipsum dolor sit am<br>consectetur adipiscing</p></div></div>
    <div class="feature" style="left:422px"><div class="badge"><svg width="24" height="22" viewBox="0 0 24 22"><path d="M12 1l10 7-10 7L2 8z" fill="#fff"/><path d="M2 12l10 7 10-7v3l-10 7-10-7z" fill="#fff"/><path d="M12 4v7M9 8l3 3 3-3" stroke="#243e63" stroke-width="2" fill="none"/></svg></div><div><h3>Icon Title Three</h3><p>Lorem ipsum dolor sit am<br>consectetur adipiscing</p></div></div>
    <div class="feature" style="left:617px"><div class="badge"><svg width="18" height="24" viewBox="0 0 18 24"><path d="M4 11V7a5 5 0 0110 0v4" stroke="#fff" stroke-width="2.5" fill="none"/><rect x="2" y="11" width="14" height="11" rx="1" fill="#fff"/><rect x="8" y="14" width="2" height="5" fill="#243e63"/></svg></div><div><h3>Icon Title Four</h3><p>Lorem ipsum dolor sit am<br>consectetur adipiscing</p></div></div>
  </section>
  <main class="content">
    <h2 class="headline" style="top:16px;width:553px">Who we are, what we do</h2>
    <div class="intro">
      <p>We are a virtual assistance/concierge company that helps the busy professional by remotely providing administrative, technical and/or creative <b>business support services</b>, specializing in the medical device industry.&nbsp; We allow things to be done without taking time away from more urgent issues or family/personal time.</p>
      <p>Partnering with a VA reduces stress, protects cash flow, eliminates administrative hassles, and enables business people to find the success they originally set out to achieve. <b>Saves small businesses</b> and/or individuals on overhead, salary, et. Work is done remotely to offer administrative, clerical, typing and specialist service assistance on a regular, ad-hoc or emergency cover basis. <span class="more">find out more &rarr;</span></p>
    </div>
    <h2 class="headline" style="top:205px;width:759px">Section two headline</h2>
    <article class="card" style="left:20px"><div class="photo" role="img" aria-label="Photo of a stressed doctor at a desk with paperwork and a laptop" style="background:linear-gradient(120deg,#e8dccb,#c9a98a 55%,#efe7dc)"></div><h4><svg width="16" height="16" viewBox="0 0 16 16"><circle cx="8" cy="8" r="8" fill="#243e63"/><path d="M4 8l3 3 5-6" stroke="#fff" stroke-width="2" fill="none"/></svg>Image title</h4><p>Lorem ipsum dolor sit am consectetur <span>&rarr;</span></p></article>
    <article class="card" style="left:285px"><div class="photo" role="img" aria-label="Photo of a doctor on the phone writing on a clipboard" style="background:linear-gradient(110deg,#f2f2f2,#dcdfe3 50%,#4a5a6a)"></div><h4><svg width="16" height="16" viewBox="0 0 16 16"><circle cx="8" cy="8" r="8" fill="#243e63"/><path d="M4 8l3 3 5-6" stroke="#fff" stroke-width="2" fill="none"/></svg>Image title</h4><p>Lorem ipsum dolor sit am consectetur <span>&rarr;</span></p></article>
    <article class="card" style="left:548px"><div class="photo" role="img" aria-label="Photo of smiling support agents wearing headsets" style="background:linear-gradient(110deg,#c8d4de,#e9d8c8 50%,#9fb4c8)"></div><h4><svg width="16" height="16" viewBox="0 0 16 16"><circle cx="8" cy="8" r="8" fill="#243e63"/><path d="M4 8l3 3 5-6" stroke="#fff" stroke-width="2" fill="none"/></svg>Image title</h4><p>Lorem ipsum dolor sit am consectetur <span>&rarr;</span></p></article>
    <blockquote class="quote">
      <svg class="mark" width="50" height="34" viewBox="0 0 50 34"><path d="M10 0h11L12 30H1z" fill="#2f6fae"/><path d="M36 0h11L38 30H27z" fill="#2f6fae"/></svg>
      <p>Lorem ipsum dolor sit amet, consectetur adipiscing elit. Integer consequat diam vitae mauris cursus et vestibulum purus gravida. - <cite>Dr. Elmer Vastberg, City Name</cite></p>
    </blockquote>
  </main>
</div>

<footer class="footer">
  <span>copyright 2012 all rights reserved</span>
  <nav><a class="active">home</a><a>about</a><a>join</a><a>blog</a><a>FAQ</a><a>contact</a></nav>
</footer>
</body>
</html>
```